The maple crew

I want it as prefession and attractive as possible we are a lawnmowing business

Phone number 605-318-2264
Name- Carlos Whitfield
Email- themaplecrewsd@fernpost.com

```html
<!DOCTYPE html>
<html lang="en">
<head>
<meta charset="utf-8">
<title>The Maple Crew – Business Cards</title>
<link href="https://fonts.googleapis.com/css2?family=Bebas+Neue&family=Inter:wght@500&display=swap" rel="stylesheet">
<style>
  :root {
    --backdrop: #002b10;
    --forest: #0c5c3a;
    --leaf: #6abf45;
    --paper: #ffffff;
  }
  * { margin: 0; padding: 0; box-sizing: border-box; }
  html, body {
    width: 1200px;
    height: 1200px;
    overflow: hidden;
    background: var(--backdrop);
  }
  .canvas { position: relative; width: 1200px; height: 1200px; }

  .card { position: absolute; overflow: hidden; }
  .card--front {
    left: 248px; top: 159px; width: 636px; height: 388px;
    background: var(--forest);
  }
  .card--back {
    left: 260px; top: 689px; width: 638px; height: 389px;
    background: var(--paper);
    box-shadow: 4px 6px 10px rgba(0,0,0,0.35);
  }

  .wordmark {
    position: absolute;
    left: 0; right: 0;
    text-align: center;
    font-family: "Bebas Neue", sans-serif;
    font-weight: 400;
    font-size: 74px;
    line-height: 1;
    letter-spacing: 2px;
    color: var(--leaf);
    white-space: nowrap;
  }
  .card--front .wordmark { top: 154px; }
  .card--back .wordmark { top: 88px; }

  .grass-band {
    position: absolute;
    left: 0; right: 0; top: 261px; height: 21px;
    background: var(--leaf);
  }
  .contact-band {
    position: absolute;
    left: 0; right: 0; top: 281px; bottom: 0;
    background: var(--forest);
  }
  .mower-scene {
    position: absolute;
    left: 0; top: 215px; width: 218px; height: 66px;
    border-radius: 6px 6px 0 0;
    background: linear-gradient(90deg, var(--leaf) 0%, var(--forest) 55%, var(--forest) 100%);
  }

  .person-name {
    position: absolute;
    left: 43px; top: 322px;
    font-family: "Bebas Neue", sans-serif;
    font-weight: 400;
    font-size: 44px;
    line-height: 1;
    letter-spacing: -0.5px;
    color: var(--leaf);
    white-space: nowrap;
  }

  .contact-list {
    position: absolute;
    left: 338px; top: 318px;
    list-style: none;
    color: var(--paper);
  }
  .contact-list li {
    display: flex;
    align-items: center;
    height: 24px;
    margin-bottom: 5px;
  }
  .contact-list svg { width: 16px; height: 16px; margin-right: 18px; flex: none; }
  .contact-phone {
    font-family: "Bebas Neue", sans-serif;
    font-size: 24px;
    letter-spacing: 0.5px;
  }
  .contact-email {
    font-family: "Inter", sans-serif;
    font-weight: 500;
    font-size: 13.5px;
  }
</style>
</head>
<body>
<main class="canvas">

  <section class="card card--front" aria-label="Business card front">
    <h1 class="wordmark">The Maple Crew</h1>
  </section>

  <section class="card card--back" aria-label="Business card back">
    <p class="wordmark">The Maple Crew</p>
    <div class="grass-band"></div>
    <div class="contact-band"></div>
    <div class="mower-scene" role="img" aria-label="Silhouette illustration of a worker pushing a lawn mower through tall grass"></div>

    <h2 class="person-name">Carlos Whitfield</h2>

    <ul class="contact-list">
      <li>
        <svg viewBox="0 0 24 24" aria-hidden="true">
          <path fill="#ffffff" d="M6.6 10.8c1.4 2.8 3.8 5.1 6.6 6.6l2.2-2.2c.3-.3.7-.4 1-.2 1.1.4 2.3.6 3.6.6.6 0 1 .4 1 1V20c0 .6-.4 1-1 1C10.6 21 3 13.4 3 4c0-.6.4-1 1-1h3.5c.6 0 1 .4 1 1 0 1.3.2 2.5.6 3.6.1.3 0 .7-.2 1z"/>
        </svg>
        <span class="contact-phone">605-318-2264</span>
      </li>
      <li>
        <svg viewBox="0 0 24 24" aria-hidden="true">
          <rect x="2.5" y="5.5" width="19" height="13" fill="none" stroke="#ffffff" stroke-width="1.5"/>
          <path d="M2.5 5.5l9.5 8 9.5-8M2.5 18.5l7-6.5M21.5 18.5l-7-6.5" fill="none" stroke="#ffffff" stroke-width="1.5"/>
        </svg>
        <span class="contact-email">themaplecrewsd@fernpost.com</span>
      </li>
    </ul>
  </section>

</main>
</body>
</html>
```